Calloway Holdings Website Design

We are a private equity firm based with offices based in Hong Kong, Singapore, London and Paris. Our focus is investments in property development projects, corporate ventures and loans.

We require the development of a new website and you will have to select relevant images from the likes of PixBarrel or other stock photo libraries.

We will need a design done for a PC based website and the designer selected with the favored design will also need to produce some concepts for a responsive website.

Target Market(s)

Sophisticated investors looking to invest in high return property development, businesses and mortgages.

Industry/Entity Type

Investment

Number of Pages Required

5+ page

Font styles to use
Serif
Sans Serif

Colors
0255a3
00a990

Requirements
Must have
• Clean modern feel and must portray stability and professionalism.

```html
<!DOCTYPE html>
<html lang="en">
<head>
<meta charset="utf-8">
<title>Calloway Holdings</title>
<link rel="stylesheet" href="https://fonts.googleapis.com/css2?family=Questrial&family=Open+Sans:wght@400;600;700&display=swap">
<style>
:root{
  --green:#0d6b12;
  --green-bright:#1f8a24;
  --navy:#1c2748;
  --nav-bg:#1e1e1e;
  --text:#444;
  --muted:#777;
  --card:#f2f2f2;
  --card-top:#dcdcdc;
  --rule:#cfcfcf;
  --footer:#3b3b3b;
  --footer-top:#333;
  --white:#fff;
}
*{margin:0;padding:0;box-sizing:border-box}
html,body{width:1200px;height:3100px;overflow:hidden}
body{position:relative;background:var(--white);font-family:"Open Sans",sans-serif;color:var(--text)}
.abs{position:absolute}
.heading{font-family:"Questrial",sans-serif}

/* nav */
.topnav{position:absolute;left:0;top:0;width:1200px;height:42px;background:var(--nav-bg)}
.topnav a{position:absolute;top:0;height:42px;line-height:42px;color:var(--white);font-family:"Questrial",sans-serif;font-size:17px;letter-spacing:.5px;text-decoration:none}
.topnav a.active{background:var(--green);padding:0 12px}
.social-squares{position:absolute;left:1037px;top:7px;display:flex;gap:5px}
.social-squares span{width:23px;height:23px;background:var(--white);border-radius:2px}

/* header */
.brandbar{position:absolute;left:0;top:42px;width:1200px;height:179px;background:linear-gradient(#ffffff,#ececec)}
.brand{position:absolute;left:0;width:1200px;top:70px;text-align:center}
.brand-dot{display:block;margin:0 auto 14px;width:38px;height:38px;border-radius:50%;background:var(--navy)}
.brand-name{font-family:"Questrial",sans-serif;font-size:30px;letter-spacing:2px;color:var(--navy)}

/* hero */
.hero{position:absolute;left:0;top:221px;width:1200px;height:471px;background:linear-gradient(180deg,#3a3a3a 0%,#262626 45%,#4a4a4a 70%,#1b1b1b 100%)}
.hero-title{position:absolute;top:128px;width:1200px;text-align:center;color:var(--white);font-family:"Questrial",sans-serif;font-size:42px;letter-spacing:1px}
.hero-title em{font-style:normal;color:var(--green-bright)}
.hero-sub{position:absolute;top:192px;left:180px;width:840px;text-align:center;color:var(--white);font-size:21px;line-height:28px;letter-spacing:.5px}
.btn{position:absolute;top:306px;height:42px;line-height:40px;text-align:center;color:var(--white);font-family:"Questrial",sans-serif;font-size:16px;letter-spacing:1px}
.btn-outline{left:442px;width:148px;border:2px solid #ddd}
.btn-solid{left:604px;width:150px;background:var(--green)}

/* section titles */
.section-title{position:absolute;left:0;width:1200px;text-align:center;font-family:"Questrial",sans-serif;font-size:25px;letter-spacing:1.5px;color:var(--navy)}
.section-title em{font-style:normal;color:var(--green)}
.divider{position:absolute;left:96px;width:1008px;height:2px;background:var(--rule)}
.divider::after{content:"";position:absolute;left:490px;top:-13px;width:26px;height:26px;border-radius:50%;background:var(--white);border:2px solid var(--rule)}
.divider.dark{background:#9a9a9a}
.divider.dark::after{background:#2d2d2d;border-color:#9a9a9a}

.intro{position:absolute;left:156px;width:888px;text-align:center;font-size:16.5px;line-height:28px;letter-spacing:.3px;color:#555}
.subhead{position:absolute;left:0;width:1200px;top:1048px;text-align:center;font-size:21px;letter-spacing:1.5px;color:var(--green);font-family:"Questrial",sans-serif}

/* cards */
.card{position:absolute;width:415px;height:134px;background:var(--card);border-top:4px solid var(--card-top)}
.card-icon{position:absolute;left:32px;top:27px;width:62px;height:62px;border-radius:50%;background:var(--green)}
.card-icon svg{width:62px;height:62px}
.card-title{position:absolute;left:115px;top:20px;font-family:"Questrial",sans-serif;font-size:19px;color:#333;letter-spacing:.5px;line-height:24px;width:280px}
.card-text{position:absolute;left:115px;width:280px;font-size:15.5px;line-height:21px;color:#555}

/* news */
.news{position:absolute;left:0;top:1675px;width:1200px;height:610px;background:linear-gradient(160deg,#2c2c2c,#161616 55%,#2a2a2a)}
.news .section-title{color:var(--white)}
.news-intro{position:absolute;left:70px;top:148px;width:1060px;text-align:center;color:var(--white);font-size:16px;line-height:30px}
.news-item{position:absolute;top:237px;width:253px}
.news-photo{width:253px;height:165px;border:4px solid #8c8c8c}
.news-title{margin-top:20px;color:var(--white);font-family:"Questrial",sans-serif;font-weight:700;font-size:18px;line-height:21px;letter-spacing:.5px}
.news-meta{margin-top:2px;color:#aaa;font-size:13px}
.news-meta span{margin-right:22px}
.news-text{margin-top:3px;color:var(--white);font-size:15px;line-height:19px}

/* testimonials */
.client{position:absolute;top:2466px;width:420px}
.client-photo{position:absolute;left:0;top:0;width:104px;height:104px;border-radius:50%;border:4px solid #ccc}
.client-name{position:absolute;left:117px;top:0;font-family:"Questrial",sans-serif;font-size:16px;letter-spacing:1px;color:#333}
.client-role{position:absolute;left:117px;top:22px;font-size:12px;font-weight:600;color:#777}
.client-quote{position:absolute;left:117px;top:46px;width:290px;font-size:13.5px;line-height:22px;color:#888}
.client-quote b{color:var(--green);font-size:26px;font-family:Georgia,serif;line-height:0;vertical-align:-6px;margin-right:4px}

/* footer */
.footer{position:absolute;left:0;top:2704px;width:1200px;height:348px;background:var(--footer);border-top:40px solid var(--footer-top)}
.f-col{position:absolute;top:66px;color:var(--white)}
.f-col h4{font-family:"Questrial",sans-serif;font-weight:400;font-size:17px;letter-spacing:1px;margin-bottom:34px}
.f-col li{list-style:none;font-size:15px;height:35.5px}
.f-col li::before{content:"›";font-weight:700;margin-right:5px}
.f-col p{font-size:15px;line-height:28px}
.f-brand{position:absolute;left:900px;top:130px;width:200px;text-align:center}
.f-brand .brand-dot{background:#9a9a9a;width:46px;height:46px}
.f-brand .brand-name{color:#9a9a9a;font-size:24px}

.bottombar{position:absolute;left:0;top:3052px;width:1200px;height:48px;background:var(--green)}
.copy{position:absolute;left:106px;top:14px;color:var(--white);font-size:14px}
.bottom-social{position:absolute;left:976px;top:12px;display:flex;gap:9px}
.bottom-social span{width:25px;height:25px;border-radius:50%;background:var(--white)}
</style>
</head>
<body>

<nav class="topnav">
  <a class="active" style="left:69px">HOME</a>
  <a style="left:198px">SERVICES</a>
  <a style="left:344px">INVESTMENT APPROACH</a>
  <a style="left:621px">MISSIONS AND VALUES</a>
  <a style="left:887px">CONTACT US</a>
  <div class="social-squares"><span></span><span></span><span></span><span></span></div>
</nav>

<header class="brandbar">
  <div class="brand" style="top:26px">
    <span class="brand-dot"></span>
    <span class="brand-name">CALLOWAY HOLDINGS</span>
  </div>
</header>

<section class="hero" role="img" aria-label="Black and white city skyline at night reflected in water">
  <h1 class="hero-title">COMPANY’S <em>SLOGAN</em> OR HEADER TEXT HERE</h1>
  <p class="hero-sub">Our mission is to provide investors with a strong foundation of core business investments that foster solid growth.</p>
  <span class="btn btn-outline">READ MORE</span>
  <span class="btn btn-solid">CONTACT US</span>
</section>

<h2 class="section-title" style="top:730px">WHO <em>WE</em> ARE?</h2>
<div class="divider" style="top:784px"></div>
<p class="intro" style="top:819px">Calloway Holdings is a is a boutique independent investment group that specializes in direct investments along with the provision of consulting and fund raising services to both established and emerging private companies. We are attracted to challenging assignments.</p>
<p class="intro" style="top:929px">With significant years of combined industry experience and international presence, we continually build upon our trusted relationships with principal partners to create successful and enduring investment partnerships. We trust, respect and like the people with whom we choose to work.</p>
<h3 class="subhead">OUR MARKETING EFFORTS EMBRACE:</h3>

<div class="card" style="left:160px;top:1108px">
  <div class="card-icon"><svg viewBox="0 0 62 62"><circle cx="31" cy="34" r="11" fill="#fff"/><rect x="26" y="18" width="10" height="6" rx="2" fill="#fff"/></svg></div>
  <div class="card-title">Our own funds</div>
  <p class="card-text" style="top:44px">Lorem ipsum dolor sit amet, consectetur adipiscing elit giat.</p>
</div>
<div class="card" style="left:623px;top:1108px">
  <div class="card-icon"><svg viewBox="0 0 62 62"><circle cx="31" cy="25" r="7" fill="#fff"/><path d="M19 44a12 11 0 0 1 24 0z" fill="#fff"/></svg></div>
  <div class="card-title">Institutional investors</div>
  <p class="card-text" style="top:44px">Lorem ipsum dolor sit amet, consectetur adipiscing elit giat.</p>
</div>
<div class="card" style="left:160px;top:1283px">
  <div class="card-icon"><svg viewBox="0 0 62 62"><circle cx="22" cy="27" r="5" fill="#fff"/><circle cx="40" cy="27" r="5" fill="#fff"/><circle cx="31" cy="24" r="6" fill="#fff"/><path d="M14 42a8 8 0 0 1 16 0zM32 42a8 8 0 0 1 16 0zM21 42a10 10 0 0 1 20 0z" fill="#fff"/></svg></div>
  <div class="card-title">Advisors and Consultants</div>
  <p class="card-text" style="top:44px">Lorem ipsum dolor sit amet, consectetur adipiscing elit giat.</p>
</div>
<div class="card" style="left:623px;top:1283px">
  <div class="card-icon"><svg viewBox="0 0 62 62"><circle cx="31" cy="31" r="6" fill="#fff"/><g stroke="#fff" stroke-width="3" stroke-linecap="round"><path d="M31 16v6M31 40v6M16 31h6M40 31h6M21 21l4 4M37 37l4 4M41 21l-4 4M21 41l4-4"/></g></svg></div>
  <div class="card-title">Strategic corporate<br>investors</div>
  <p class="card-text" style="top:68px">Lorem ipsum dolor sit amet, consectetur adipiscing elit giat.</p>
</div>
<div class="card" style="left:160px;top:1458px">
  <div class="card-icon"><svg viewBox="0 0 62 62"><g fill="#fff"><rect x="18" y="36" width="5" height="8"/><rect x="25" y="31" width="5" height="13"/><rect x="32" y="26" width="5" height="18"/><rect x="39" y="20" width="5" height="24"/></g></svg></div>
  <div class="card-title">High net-worth individuals</div>
  <p class="card-text" style="top:44px">Lorem ipsum dolor sit amet, consectetur adipiscing elit giat.</p>
</div>

<section class="news" role="img" aria-label="Dim office background with a business meeting">
  <h2 class="section-title" style="top:55px">LATEST NEWS</h2>
  <div class="divider dark" style="top:109px"></div>
  <p class="news-intro">Lorem ipsum dolor sit amet, consectetur adipiscing elit. Ut volutpat elit ut, cursus dolo consectetur varius lacus, non rhoncus turpis pharetra et. Ut ut euismod magna. Proin non nibh dignissim, volutpat elit ut, cursus dolor.</p>
  <article class="news-item" style="left:112px">
    <div class="news-photo" role="img" aria-label="Hands around a seedling growing from coins" style="background:linear-gradient(160deg,#e9e4d8,#b8a47a 60%,#8a9a55)"></div>
    <div class="news-title">SAMPLE TITLE PLACEHOLDER</div>
    <div class="news-meta"><span>▪ Admin</span><span>▪ 1/16/16</span></div>
    <p class="news-text">Lorem ipsum dolor sit amet, consectetur adipiscing elit. Ut volutpat elit ut...</p>
  </article>
  <article class="news-item" style="left:471px">
    <div class="news-photo" role="img" aria-label="Businessman looking through binoculars" style="background:linear-gradient(160deg,#e2e2e0,#b9b6ad 55%,#55555a)"></div>
    <div class="news-title">FIRST LINE GOES HERE &amp;<br>SECOND LINE SAMPLE HERE</div>
    <div class="news-meta"><span>▪ Admin</span><span>▪ 1/16/16</span></div>
    <p class="news-text">Lorem ipsum dolor sit amet, consectetur adipiscing elit. Ut volutpat elit ut...</p>
  </article>
  <article class="news-item" style="left:829px">
    <div class="news-photo" role="img" aria-label="Glasses and pen lying on financial charts" style="background:linear-gradient(160deg,#3a4d7a,#b5622a 55%,#e0a04a)"></div>
    <div class="news-title">ARTICLE TITLE SAMPLE ONLY</div>
    <div class="news-meta"><span>▪ Admin</span><span>▪ 1/16/16</span></div>
    <p class="news-text">Lorem ipsum dolor sit amet, consectetur adipiscing elit. Ut volutpat elit ut...</p>
  </article>
</section>

<h2 class="section-title" style="top:2347px">WHAT <em>ARE</em> CLIENTS SAY</h2>
<div class="divider" style="top:2400px"></div>

<div class="client" style="left:138px">
  <div class="client-photo" role="img" aria-label="Portrait of a client" style="background:linear-gradient(#d8d8d8,#6a6a6a)"></div>
  <div class="client-name">JOHN DOE</div>
  <div class="client-role">President, Company name</div>
  <p class="client-quote"><b>“</b>Lorem ipsum dolor sit amet, con secte-tur adipiscing elit. Phasellus tincidunt tellus leo, sodales vestibulum urna. hen-drerit vel. Maecenas ut pretium tortor.</p>
</div>
<div class="client" style="left:648px">
  <div class="client-photo" role="img" aria-label="Portrait of a client" style="background:linear-gradient(#d8d8d8,#6a6a6a)"></div>
  <div class="client-name">GEORGE SMITH</div>
  <div class="client-role">VP Sales, Company name</div>
  <p class="client-quote"><b>“</b>Lorem ipsum dolor sit amet, con secte-tur adipiscing elit. Phasellus tincidunt tellus leo, sodales vestibulum urna. hen-drerit vel. Maecenas ut pretium tortor.</p>
</div>

<footer class="footer">
  <div class="f-col" style="left:110px">
    <h4>Quicklinks</h4>
    <ul><li>Sublink 1</li><li>Sublink 2</li><li>Sublink 3</li><li>Sublink 4</li></ul>
  </div>
  <div class="f-col" style="left:352px">
    <h4>Useful Info</h4>
    <ul><li>FAQ</li><li>Sitemap</li><li>Terms &amp; Agreement</li><li>Privacy Policy</li></ul>
  </div>
  <div class="f-col" style="left:590px">
    <h4>Contact us</h4>
    <p>Calloway Holdings<br>1111 Lorem Ipsum Bldg<br>Ipsumville, NY 22578<br>P: (111) 222-3333</p>
  </div>
  <div class="f-brand" style="top:66px">
    <span class="brand-dot"></span>
    <span class="brand-name">CALLOWAY HOLDINGS</span>
  </div>
</footer>

<div class="bottombar">
  <span class="copy">© 2016 Calloway Holdings</span>
  <div class="bottom-social"><span></span><span></span><span></span></div>
</div>

</body>
</html>
```